Business Card Design Project

We need a business card for our new business based in Vancouver called
"Sollu Calm Spa" We are looking for a simple yet bold design for our business cards that will enable us to stand out from the pack. All business card details will be provided in the handover stage.
Updates

Thank you to all who have submitted

The work is great for the most part
Cards with creative use of the logo
have been more successful so far

Dark cards and rounded edges 
are also getting good reviews

Double sided is an option we would like to see explored

Thank you

Target Market(s)

Our clients are stressed business people, yoga/meditation enthusiast, and people looking for a new experience in a Spa enviroment

Industry/Entity Type

Business

Font styles to use
Other font styles liked:
• please check design file

Requirements
Must have
• Sollu Calm Spa

2417 E Fenwick Row, Vancouver, BC V5K 3H9

sollu@calmspa-example.ca
Nice to have
• Creative approach to layout and design

Outside of the box design elements
Should not have
• Should not be too busy

```html
<!DOCTYPE html>
<html lang="en">
<head>
<meta charset="utf-8">
<title>Sollu Calm Spa — Business Card</title>
<link href="https://fonts.googleapis.com/css2?family=Jost:wght@300;500&display=swap" rel="stylesheet">
<style>
  :root {
    --page-bg: #eeeeee;
    --card-bg: #6e6e70;
    --card-ink: #ffffff;
  }
  * { box-sizing: border-box; margin: 0; padding: 0; }
  html, body {
    width: 1200px;
    height: 1000px;
    overflow: hidden;
    background: var(--page-bg);
  }
  .card {
    position: absolute;
    left: 120px;
    top: 200px;
    width: 960px;
    height: 600px;
    background: var(--card-bg);
    overflow: hidden;
    font-family: "Jost", "Futura", sans-serif;
    color: var(--card-ink);
  }
  .brand {
    position: absolute;
    left: 142px;
    top: 124px;
    display: flex;
    align-items: center;
    gap: 20px;
  }
  .brand__dot {
    width: 52px;
    height: 52px;
    border-radius: 50%;
    border: 2px solid var(--card-ink);
    flex: none;
  }
  .brand__name {
    font-weight: 300;
    font-size: 48px;
    line-height: 1;
    letter-spacing: 1px;
    white-space: nowrap;
  }
  .contact {
    position: absolute;
    left: 478px;
    top: 296px;
    font-weight: 300;
    font-size: 25px;
    line-height: 33px;
    font-style: normal;
  }
  .contact__email {
    margin-top: 66px;
    display: block;
  }
  .contact__email strong { font-weight: 500; }
</style>
</head>
<body>
  <section class="card" aria-label="Sollu Calm Spa business card, front">
    <div class="brand">
      <span class="brand__dot" aria-hidden="true"></span>
      <span class="brand__name">Sollu Calm Spa</span>
    </div>

    <address class="contact">
      <span class="contact__line">2417 E Fenwick Row</span><br>
      <span class="contact__line">Vancouver, BC</span><br>
      <span class="contact__line">V5K 3H9</span>
      <span class="contact__email">sollu<strong>@calmspa-example.ca</strong></span>
    </address>
  </section>
</body>
</html>
```